Business card design for Sable Crestway

We need business cards designed for our new marketing consulting company, Sable Crestway. Our services include marketing strategy, go-to-market and launch planning, growth strategy, and execution. We serve medical technology and health technology companies, from startups to well-established growth companies.

The business cards should feel professional, credible, reliable and trustworthy, and should instill confidence. Also bold, creative, and modern.

The design must use the Sable Crestway logo.

The primary brand color is this orange: #FF5501
A secondary color that you can use is this gray: #282B2D
I would prefer only to use the orange and gray. But if you feel you really need an additional accent color (please use it very sparingly, as little as possible), you can use this blue for small accent purposes: #009FED

Attached are the logo files. The main logo is the one with a little bit of orange on the left and the rest is gray.

The business card should include the following:

Sable Crestway logo
First name and last name
Title
Email address
Phone number and type (in whatever order looks best for the design
Website (the website does not need to be in the same block as the personal info)

For example:

Wren Tasker
Founder & Principal
wren@sablecrestway.com
+1.415.836.2094 mobile (can use "." or spaces in between blocks of numbers)
sablecrestway.com (somewhere on the card, it does not need to be with the personal info; and note that there is no "www." at the beginning)

Note that there will be no address listed on the business card.

Target Market(s)

Executives (CEO, head of marketing, head of sales) at medical technology and health technology companies, mostly in their 40s and older, well-educated, often with advanced degrees. They are strategic thinkers, responsible for budgets, and familiar with P&L. Their comfort with and trust in using outside consultants varies.

Industry/Entity Type

Medical technology and health technology companies.

Contact Information for Business Card

See project description

Font styles to use
Sans Serif

Requirements
Must have
• Logo and see Business card details section above.

```html
<!DOCTYPE html>
<html lang="en">
<head>
<meta charset="utf-8">
<title>Sable Crestway — Business Card</title>
<link href="https://fonts.googleapis.com/css2?family=Poppins:wght@400;500;600;700&display=swap" rel="stylesheet">
<style>
  :root {
    --brand-orange: #f05a24;
    --brand-gray: #282b2d;
    --card-white: #ffffff;
    --stage: #222222;
    --text-dark: #1f2123;
  }
  * { margin: 0; padding: 0; box-sizing: border-box; }
  html, body {
    width: 1200px;
    height: 711px;
    overflow: hidden;
    background: var(--stage);
    font-family: "Poppins", sans-serif;
  }
  .canvas {
    width: 1200px;
    height: 711px;
    display: flex;
    align-items: center;
    justify-content: center;
    gap: 40px;
  }
  .card {
    position: relative;
    width: 540px;
    height: 310px;
    border-radius: 22px;
    overflow: hidden;
  }
  .card--front {
    background: var(--brand-orange);
    display: flex;
    align-items: center;
    justify-content: center;
  }
  .card--back {
    background: var(--card-white);
    border-bottom: 4px solid var(--brand-orange);
  }

  .brand {
    display: flex;
    align-items: center;
    gap: 14px;
  }
  .brand__dot {
    border-radius: 50%;
    flex: none;
  }
  .brand__name {
    font-weight: 600;
    text-transform: uppercase;
    letter-spacing: 0.14em;
    line-height: 1.05;
  }
  .card--front .brand__dot { width: 58px; height: 58px; background: var(--card-white); }
  .card--front .brand__name { color: var(--card-white); font-size: 34px; }

  .card--back .brand {
    position: absolute;
    left: 34px;
    top: 118px;
    gap: 10px;
  }
  .card--back .brand__dot { width: 30px; height: 30px; background: var(--brand-orange); }
  .card--back .brand__name { color: var(--brand-gray); font-size: 19px; }

  .divider {
    position: absolute;
    left: 262px;
    top: 60px;
    width: 1px;
    height: 170px;
    background: var(--brand-orange);
  }

  .contact {
    position: absolute;
    left: 292px;
    top: 78px;
    color: var(--text-dark);
  }
  .contact__name {
    font-size: 26px;
    line-height: 1.1;
    font-weight: 400;
    color: var(--brand-gray);
  }
  .contact__first {
    font-weight: 700;
    color: var(--brand-orange);
  }
  .contact__title {
    font-size: 12.5px;
    font-weight: 500;
    margin-top: 2px;
  }
  .contact__list {
    list-style: none;
    margin-top: 18px;
    font-size: 12.5px;
  }
  .contact__item {
    display: flex;
    align-items: center;
    gap: 8px;
    margin-bottom: 6px;
  }
  .contact__icon { width: 13px; height: 13px; flex: none; }

  .website {
    position: absolute;
    right: 40px;
    bottom: 26px;
    font-size: 14px;
    color: var(--brand-orange);
  }
</style>
</head>
<body>
<main class="canvas">
  <section class="card card--front" aria-label="Card front">
    <div class="brand">
      <span class="brand__dot"></span>
      <span class="brand__name">Sable<br>Crestway</span>
    </div>
  </section>

  <section class="card card--back" aria-label="Card back">
    <div class="brand">
      <span class="brand__dot"></span>
      <span class="brand__name">Sable<br>Crestway</span>
    </div>

    <div class="divider"></div>

    <div class="contact">
      <p class="contact__name"><span class="contact__first">Wren</span> Tasker</p>
      <p class="contact__title">Founder &amp; Principal</p>
      <ul class="contact__list">
        <li class="contact__item">
          <svg class="contact__icon" viewBox="0 0 24 24" aria-hidden="true">
            <path fill="var(--brand-orange)" d="M6.6 10.8a15.1 15.1 0 0 0 6.6 6.6l2.2-2.2a1 1 0 0 1 1-.25 11.4 11.4 0 0 0 3.6.57 1 1 0 0 1 1 1V20a1 1 0 0 1-1 1A17 17 0 0 1 3 4a1 1 0 0 1 1-1h3.5a1 1 0 0 1 1 1c0 1.25.2 2.45.57 3.6a1 1 0 0 1-.25 1z"/>
          </svg>
          <span>+1.415.836.2094</span>
        </li>
        <li class="contact__item">
          <svg class="contact__icon" viewBox="0 0 24 24" aria-hidden="true">
            <rect x="2" y="5" width="20" height="14" rx="2" fill="var(--brand-orange)"/>
            <path d="M3 6.5l9 6.5 9-6.5" fill="none" stroke="#fff" stroke-width="1.8"/>
          </svg>
          <span>wren@sablecrestway.com</span>
        </li>
      </ul>
    </div>

    <p class="website">sablecrestway.com</p>
  </section>
</main>
</body>
</html>
```